Korvath Networks, Inc. Website redesign

Revamp the website, it is old and outdated. www.korvathnetworksinc.example

Target Market(s)

Information Technology Consulting and Staffing

Coding

Coded - Design and coding required

Number of Pages Required

5+ page

Colors

Designer to choose colors to be used in the design.

Requirements
Must have
• Outlined text boxes just like from the Quillbright.example site. A clean look

```html
<!DOCTYPE html>
<html lang="en">
<head>
<meta charset="utf-8">
<title>Korvath Networks, Inc. – Reliable IT Solutions</title>
<link rel="stylesheet" href="https://fonts.googleapis.com/css2?family=Montserrat:wght@600;700&family=Open+Sans:wght@400;600;700&display=swap">
<style>
:root{
  --navy:#1c3766;
  --navy-dark:#0f2240;
  --teal:#19a3c6;
  --teal-light:#7fd3e6;
  --mist:#eaf6fa;
  --red:#c41e2e;
  --ink:#3b4350;
  --muted:#7b8390;
  --line:#d9dee5;
  --white:#ffffff;
}
*{margin:0;padding:0;box-sizing:border-box}
html,body{width:1200px;height:2936px;overflow:hidden}
body{font-family:"Open Sans",Arial,sans-serif;color:var(--ink);background:var(--white);position:relative}
h1,h2,h3{font-family:"Montserrat",Arial,sans-serif;color:var(--navy)}
a{text-decoration:none;color:inherit}
.btn{display:inline-block;background:var(--red);color:var(--white);font-size:13px;font-weight:600;padding:10px 22px;border-radius:2px}
.read-more{color:var(--red);font-size:12px;font-weight:700}

/* hero */
.hero{position:absolute;left:0;top:0;width:1200px;height:580px;background:linear-gradient(180deg,#f4fafc,#ffffff);overflow:hidden}
.hero-wave{position:absolute;right:0;top:0}
.site-header{position:absolute;left:0;top:0;width:1200px;height:70px;display:flex;align-items:center;justify-content:space-between;padding:0 40px}
.brand{display:flex;flex-direction:column}
.brand-name{font-family:"Montserrat",Arial,sans-serif;font-weight:700;font-size:22px;color:var(--navy);white-space:nowrap}
.brand-tag{font-size:11px;color:var(--red);letter-spacing:1px;text-transform:uppercase;font-weight:600}
.main-nav{display:flex;gap:30px;font-size:13px;font-weight:600;color:var(--white)}
.hero-copy{position:absolute;left:40px;top:110px;width:500px}
.hero-copy h1{font-size:34px;line-height:1.22;margin-bottom:22px}
.hero-copy p{font-size:13px;line-height:1.7;color:var(--muted);margin-bottom:26px;width:440px}
.hero-art{position:absolute;left:580px;top:120px;width:540px;height:400px;border-radius:20px;background:linear-gradient(135deg,#ffd86b 0%,#f5b24a 40%,#5dc0da 100%);opacity:.85}

/* services */
.services{position:absolute;left:40px;top:600px;width:1120px;display:flex;gap:20px}
.service-card{flex:1;height:330px;border:1px solid var(--line);background:var(--white);padding:24px 22px;box-shadow:0 4px 14px rgba(0,0,0,.05)}
.service-icon{width:54px;height:54px;background:var(--red);border-radius:4px;display:flex;align-items:center;justify-content:center;margin-bottom:18px}
.service-card h3{font-size:15px;margin-bottom:12px}
.service-card p{font-size:11.5px;line-height:1.7;color:var(--muted);margin-bottom:14px}

/* leadership */
.leadership{position:absolute;left:0;top:970px;width:1200px;height:480px}
.leadership-art{position:absolute;left:40px;top:20px;width:520px;height:420px;border-radius:16px;background:linear-gradient(160deg,#f6c24f 0%,#5b9fd3 55%,#1c3766 100%);opacity:.85}
.leadership-copy{position:absolute;left:610px;top:80px;width:540px}
.leadership-copy h2{font-size:30px;line-height:1.25;margin-bottom:20px}
.leadership-copy p{font-size:12.5px;line-height:1.75;color:var(--muted);margin-bottom:24px}

/* strategy */
.strategy{position:absolute;left:0;top:1470px;width:1200px;height:370px;background:linear-gradient(180deg,#ffffff 0%,var(--mist) 100%);overflow:hidden}
.strategy-wave{position:absolute;right:0;top:0}
.strategy-copy{position:absolute;left:40px;top:70px;width:540px}
.strategy-copy h2{font-size:30px;line-height:1.25;margin-bottom:18px}
.strategy-copy p{font-size:12.5px;line-height:1.75;color:var(--muted);margin-bottom:22px}
.strategy-art{position:absolute;left:640px;top:30px;width:500px;height:310px;border-radius:16px;background:linear-gradient(135deg,#5ec4dc 0%,#1c3766 70%,#f3b54a 100%);opacity:.85}

/* news */
.news{position:absolute;left:0;top:1840px;width:1200px;height:690px;background:var(--white)}
.news h2{text-align:center;font-size:30px;margin-top:40px}
.news-intro{text-align:center;font-size:12.5px;color:var(--muted);width:640px;margin:12px auto 34px;line-height:1.6}
.news-grid{display:flex;gap:16px;padding:0 40px}
.news-card{flex:1;border:1px solid var(--line);background:var(--white);box-shadow:0 4px 14px rgba(0,0,0,.05)}
.news-photo{height:170px;background:linear-gradient(135deg,#c9d4df,#7f97ae);position:relative}
.news-date{position:absolute;left:10px;bottom:-12px;background:var(--red);color:var(--white);font-size:10px;font-weight:700;padding:5px 10px}
.news-body{padding:26px 14px 22px}
.news-body h3{font-size:14px;margin-bottom:10px}
.news-body p{font-size:11px;line-height:1.7;color:var(--muted);margin-bottom:14px}
.pager{display:flex;justify-content:center;gap:8px;margin-top:30px}
.pager span{width:8px;height:8px;border-radius:50%;background:var(--line)}
.pager span.active{background:var(--red)}

/* footer */
.site-footer{position:absolute;left:0;top:2530px;width:1200px;height:406px;background:var(--navy-dark);color:#c6cfdc}
.footer-cols{display:flex;padding:50px 40px 0;gap:36px}
.footer-brand{width:300px;flex:none}
.footer-brand .brand-name{color:var(--white);font-size:22px}
.footer-brand .brand-tag{color:#e0a2a8;margin:6px 0 16px}
.footer-brand p{font-size:11.5px;line-height:1.7}
.footer-col{flex:1}
.footer-col.contact{flex:1.5}
.footer-col h4{font-family:"Montserrat",Arial,sans-serif;color:var(--white);font-size:14px;margin-bottom:18px}
.footer-col li{list-style:none;font-size:11.5px;margin-bottom:10px;display:flex;gap:8px;align-items:flex-start;line-height:1.5}
.footer-col li svg{flex:none;margin-top:2px}
.footer-bottom{position:absolute;left:40px;right:40px;bottom:0;height:56px;border-top:1px solid #243a5e;display:flex;align-items:center;justify-content:center;font-size:11px}
</style>
</head>
<body>

<section class="hero">
  <svg class="hero-wave" width="760" height="580" viewBox="0 0 760 580" aria-hidden="true">
    <path d="M140 0 H760 V520 C640 560 560 470 470 430 C360 380 260 420 200 330 C140 240 260 160 200 90 C170 50 140 30 140 0 Z" fill="var(--teal)"/>
    <path d="M300 0 H760 V300 C660 330 600 260 520 220 C420 170 360 120 300 0 Z" fill="var(--teal-light)" opacity=".35"/>
  </svg>
  <header class="site-header">
    <div class="brand">
      <span class="brand-name">Korvath Networks, Inc.</span>
      <span class="brand-tag">Trust Insight Delivery</span>
    </div>
    <nav class="main-nav">
      <a href="#">Home</a><a href="#">About us</a><a href="#">Services</a><a href="#">Strategy</a><a href="#">News</a><a href="#">Contact us</a>
    </nav>
  </header>
  <div class="hero-copy">
    <h1>For over 20 + years<br>We have been Providing<br>Reliable IT Solutions</h1>
    <p>Korvath Networks, Inc. is an IT consulting and staffing firm serving clients across the region. We give our clients cutting edge technologies and dependable people.</p>
    <a class="btn" href="#">Know More</a>
  </div>
  <div class="hero-art" role="img" aria-label="Illustration of a team working on laptops and charts"></div>
</section>

<section class="services">
  <article class="service-card">
    <div class="service-icon"><svg width="26" height="26" viewBox="0 0 26 26" fill="none" stroke="#fff" stroke-width="2"><rect x="3" y="4" width="20" height="13" rx="1"/><path d="M9 22h8M13 17v5"/></svg></div>
    <h3>Hardware / Software Sales</h3>
    <p>We help clients choose and buy the right hardware and software for their needs. Our team compares vendors, sets fair pricing and delivers systems that are ready to run from day one.</p>
    <a class="read-more" href="#">Read More</a>
  </article>
  <article class="service-card">
    <div class="service-icon"><svg width="26" height="26" viewBox="0 0 26 26" fill="none" stroke="#fff" stroke-width="2"><circle cx="13" cy="8" r="4"/><path d="M5 23c0-5 4-8 8-8s8 3 8 8"/></svg></div>
    <h3>Professional Services</h3>
    <p>Our skilled consultants and staff support your projects from planning to delivery. We place the right people on the right work so your teams can focus on growth and results.</p>
    <a class="read-more" href="#">Read More</a>
  </article>
  <article class="service-card">
    <div class="service-icon"><svg width="26" height="26" viewBox="0 0 26 26" fill="none" stroke="#fff" stroke-width="2"><path d="M6 3h10l4 4v16H6z"/><path d="M9 13l3 3 5-6"/></svg></div>
    <h3>Technology Assessment</h3>
    <p>We review your current systems, find the gaps and risks, and map a clear plan forward. Each assessment ends with practical steps your business can act on right away.</p>
    <a class="read-more" href="#">Read More</a>
  </article>
  <article class="service-card">
    <div class="service-icon"><svg width="26" height="26" viewBox="0 0 26 26" fill="none" stroke="#fff" stroke-width="2"><circle cx="13" cy="13" r="9"/><path d="M13 8v5l3 3"/></svg></div>
    <h3>Technology Consulting</h3>
    <p>Our advisors help you match technology with your business goals. From strategy to rollout, we guide each decision so your investment brings lasting value to the company.</p>
    <a class="read-more" href="#">Read More</a>
  </article>
</section>

<section class="leadership">
  <div class="leadership-art" role="img" aria-label="Illustration of a team meeting around a table with a light bulb idea"></div>
  <div class="leadership-copy">
    <h2>Bringing Thought Leadership and Quality to Every Project</h2>
    <p>Korvath Networks, Inc. is a trusted IT consulting company with decades of experience. We offer specialized, highly customized technology solutions for our clients in many industries. Our services span the full project life cycle, from early planning through support after launch.</p>
    <p>We believe strong technology supports every part of a business. Every engagement starts with a careful review of your needs, and our people stay with you until the work is done right and your teams feel confident.</p>
    <a class="btn" href="#">Read More</a>
  </div>
</section>

<section class="strategy">
  <svg class="strategy-wave" width="620" height="370" viewBox="0 0 620 370" aria-hidden="true">
    <path d="M620 0 V370 H120 C220 330 260 250 340 220 C440 180 520 120 620 0 Z" fill="var(--teal)" opacity=".2"/>
  </svg>
  <div class="strategy-copy">
    <h2>Our Strategy Your Path to Success</h2>
    <p>Clients and partners count on us to deliver steady progress while they manage change, growth and daily operations. We shape every plan around your goals, your people and your budget, so each step adds clear value and keeps your business moving with confidence.</p>
    <a class="btn" href="#">Read More</a>
  </div>
  <div class="strategy-art" role="img" aria-label="Illustration of business people holding large keys beside a keyhole"></div>
</section>

<section class="news">
  <h2>IT News</h2>
  <p class="news-intro">Lorem ipsum dolor sit amet, consectetur adipiscing elit. Duis sed pellentesque massa. Curabitur viverra imperdiet sapien, nec ullamcorper sapien. Nullam pharetra maximus dolor.</p>
  <div class="news-grid">
    <article class="news-card"><div class="news-photo" role="img" aria-label="Photo of a professional at work"><span class="news-date">Aug 17, 2019</span></div><div class="news-body"><h3>Lorem ipsum dolor</h3><p>Vivamus euismod nunc ut tristique mattis. Donec nibh metus, commodo quis diam, luctus pharetra nibh.</p><a class="read-more" href="#">Read More...</a></div></article>
    <article class="news-card"><div class="news-photo" role="img" aria-label="Photo of a team meeting"><span class="news-date">Aug 17, 2019</span></div><div class="news-body"><h3>Lorem ipsum dolor</h3><p>Vivamus euismod nunc ut tristique mattis. Donec nibh metus, commodo quis diam, luctus pharetra nibh.</p><a class="read-more" href="#">Read More...</a></div></article>
    <article class="news-card"><div class="news-photo" role="img" aria-label="Photo of colleagues at a desk"><span class="news-date">Aug 17, 2019</span></div><div class="news-body"><h3>Lorem ipsum dolor</h3><p>Vivamus euismod nunc ut tristique mattis. Donec nibh metus, commodo quis diam, luctus pharetra nibh.</p><a class="read-more" href="#">Read More...</a></div></article>
    <article class="news-card"><div class="news-photo" role="img" aria-label="Photo of a business discussion"><span class="news-date">Aug 17, 2019</span></div><div class="news-body"><h3>Lorem ipsum dolor</h3><p>Vivamus euismod nunc ut tristique mattis. Donec nibh metus, commodo quis diam, luctus pharetra nibh.</p><a class="read-more" href="#">Read More...</a></div></article>
    <article class="news-card"><div class="news-photo" role="img" aria-label="Photo of a consultant with a laptop"><span class="news-date">Aug 17, 2019</span></div><div class="news-body"><h3>Lorem ipsum dolor</h3><p>Vivamus euismod nunc ut tristique mattis. Donec nibh metus, commodo quis diam, luctus pharetra nibh.</p><a class="read-more" href="#">Read More...</a></div></article>
  </div>
  <div class="pager"><span class="active"></span><span></span><span></span></div>
</section>

<footer class="site-footer">
  <div class="footer-cols">
    <div class="footer-brand">
      <div class="brand-name">Korvath Networks, Inc.</div>
      <div class="brand-tag">Trust Insight Delivery</div>
      <p>Korvath Networks, Inc. has been a leading IT consulting and staffing firm for over twenty years, helping clients find the right people and the right technology to succeed.</p>
    </div>
    <div class="footer-col contact">
      <h4>Contact Us</h4>
      <ul>
        <li><svg width="12" height="14" viewBox="0 0 12 14" fill="#c41e2e"><path d="M6 0a5 5 0 0 1 5 5c0 4-5 9-5 9S1 9 1 5a5 5 0 0 1 5-5zm0 3a2 2 0 1 0 0 4 2 2 0 0 0 0-4z"/></svg>4 Harbor Row, Suite 210,<br>Westfield, NJ 07090</li>
        <li><svg width="12" height="12" viewBox="0 0 12 12" fill="#c41e2e"><path d="M2 0l2 3-1 1.5a7 7 0 0 0 3.5 3.5L8 7l3 2-1 2.5C5 11.5.5 7 .5 2z"/></svg>(201) 555-0148</li>
        <li><svg width="12" height="10" viewBox="0 0 12 10" fill="none" stroke="#c41e2e" stroke-width="1.4"><rect x=".7" y=".7" width="10.6" height="8.6"/><path d="M1 1l5 4 5-4"/></svg>hello@korvathnetworksinc.example</li>
      </ul>
    </div>
    <div class="footer-col">
      <h4>Our Services</h4>
      <ul><li>Hardware / Software Sales</li><li>Professional Services</li><li>Technology Assessment</li><li>Technology Consulting</li></ul>
    </div>
    <div class="footer-col">
      <h4>Our Strategy</h4>
      <ul><li>Bringing Thought Leadership and Quality to Every Project</li><li>Our Strategy Your Path to Success</li></ul>
    </div>
    <div class="footer-col">
      <h4>Follow Us</h4>
      <ul>
        <li><svg width="12" height="12" viewBox="0 0 12 12"><circle cx="6" cy="6" r="6" fill="#c41e2e"/></svg>Social Page</li>
        <li><svg width="12" height="12" viewBox="0 0 12 12"><circle cx="6" cy="6" r="6" fill="#c41e2e"/></svg>Career Page</li>
      </ul>
    </div>
  </div>
  <div class="footer-bottom">© 2019 Korvath Networks, Inc. All Rights Reserved.</div>
</footer>

</body>
</html>
```